Clean professional design needed for landscape property business

We need a logo for a new lawncare, landscaping , property maintenance business called Meadow Trim.
Our services include lawn mowing, garden maintenance, clean ups and some property maintenance.
We want a double sided business card that is clean and very professional using the colour scheme from our logo which is provided.
the business card should have impact as we will use these to drop into people's letterboxes as a marketing drop.
Initially we want to see what you come up with so there is a very wide scope here to work with.
Updates

Project Deadline Extended
Reason: we feel our original deadline was too short. we have extended to give more time for quality submissions.

Target Market(s)

High end property owners who don't wish to do there own gardneing or property maintenance

Industry/Entity Type

Business

Contact Information for Business Card

Name
Postion/ Title
Phone number
mobile
web address
physical address

services offered

Font styles to use
Sans Serif

Requirements
Must have
• curved edges preferrred
Nice to have
• We like the idea of the logo being embossed or etched into the card so it looks like it is below the surface of the card
Should not have
• No stock images or characters.

```html
<!DOCTYPE html>
<html lang="en">
<head>
<meta charset="utf-8">
<title>Meadow Trim – Business Card</title>
<link rel="stylesheet" href="https://fonts.googleapis.com/css2?family=Source+Sans+3:wght@400;600;700&display=swap">
<style>
  :root {
    --green: #7cb81f;
    --charcoal: #58585b;
    --ink: #4a4a4c;
    --rule: #9a9a9a;
    --paper: #ffffff;
    --backdrop: #e8e5e1;
  }
  * { margin: 0; padding: 0; box-sizing: border-box; }
  html, body { width: 1200px; height: 987px; overflow: hidden; }
  body {
    background: var(--backdrop);
    font-family: "Source Sans 3", Arial, sans-serif;
    color: var(--ink);
    position: relative;
  }
  .card {
    position: absolute;
    left: 293px;
    width: 615px;
    height: 350px;
    border-radius: 20px;
    overflow: hidden;
    box-shadow: 0 4px 14px rgba(0,0,0,.18);
  }
  .card-front { top: 131px; background: var(--paper); }
  .card-back  { top: 506px; background: var(--charcoal); }

  .wordmark {
    position: absolute;
    display: flex;
    align-items: center;
    gap: 12px;
    font-weight: 700;
    letter-spacing: -1px;
    white-space: nowrap;
  }
  .wordmark-dot { border-radius: 50%; background: var(--green); }
  .card-front .wordmark { left: 30px; top: 56px; font-size: 42px; color: var(--charcoal); }
  .card-front .wordmark-dot { width: 16px; height: 16px; }

  .identity { position: absolute; right: 35px; top: 172px; text-align: right; }
  .identity-name { font-size: 21px; font-weight: 700; color: var(--green); letter-spacing: .3px; line-height: 1.1; }
  .identity-title { font-size: 16px; color: var(--ink); line-height: 1.3; }

  .divider { position: absolute; left: 32px; right: 35px; top: 226px; height: 1px; background: var(--rule); }

  .address { position: absolute; left: 32px; top: 263px; font-size: 16px; line-height: 23px; }

  .contacts { position: absolute; right: 35px; top: 237px; list-style: none; font-size: 16px; line-height: 23.5px; text-align: right; }
  .contacts li { display: flex; justify-content: flex-end; align-items: center; gap: 9px; }
  .contacts svg { width: 14px; height: 14px; fill: var(--green); }

  .footer-strip { position: absolute; left: 0; bottom: 0; width: 615px; height: 30px; }
  .website {
    position: absolute; right: 18px; bottom: 5px;
    font-size: 15px; color: #fff; letter-spacing: 3px;
  }

  .card-back .wordmark {
    left: 0; right: 0; top: 132px; justify-content: center;
    font-size: 58px; color: #fff;
  }
  .card-back .wordmark-dot { width: 22px; height: 22px; }
  .services {
    position: absolute; left: 0; right: 0; top: 275px;
    text-align: center; color: #fff; font-size: 17px; line-height: 20px;
  }
  .services-dot {
    display: inline-block; width: 7px; height: 7px; border-radius: 50%;
    background: var(--green); margin: 0 4px; vertical-align: middle;
  }
</style>
</head>
<body>

<section class="card card-front" aria-label="Business card front">
  <div class="wordmark"><span>meadowtrim</span><span class="wordmark-dot"></span></div>

  <div class="identity">
    <div class="identity-name">DANIEL BROOKS</div>
    <div class="identity-title">CEO&amp;Founder</div>
  </div>

  <div class="divider"></div>

  <address class="address" style="font-style:normal">
    4120 Willow Creek Road<br>
    Fairbanks, Alaska 99701
  </address>

  <ul class="contacts">
    <li>(555) 214-7302
      <svg viewBox="0 0 24 24" aria-hidden="true"><path d="M6.6 10.8a15.1 15.1 0 0 0 6.6 6.6l2.2-2.2c.3-.3.7-.4 1-.2 1.1.4 2.3.6 3.6.6.6 0 1 .4 1 1V20c0 .6-.4 1-1 1A17 17 0 0 1 3 4c0-.6.4-1 1-1h3.5c.6 0 1 .4 1 1 0 1.3.2 2.5.6 3.6.1.3 0 .7-.2 1z"/></svg>
    </li>
    <li>(555) 318-6071
      <svg viewBox="0 0 24 24" aria-hidden="true"><path d="M7 1h10a2 2 0 0 1 2 2v18a2 2 0 0 1-2 2H7a2 2 0 0 1-2-2V3a2 2 0 0 1 2-2zm0 3v15h10V4zm5 16.2a1 1 0 1 0 0 .1z"/></svg>
    </li>
    <li>daniel@meadowtrim.com
      <svg viewBox="0 0 24 24" aria-hidden="true"><path d="M2 5h20v14H2zm2 2v.4l8 5 8-5V7zm0 2.8V17h16V9.8l-8 5z"/></svg>
    </li>
  </ul>

  <svg class="footer-strip" viewBox="0 0 615 30" preserveAspectRatio="none">
    <rect x="0" y="17" width="340" height="9" fill="#7cb81f" role="img" aria-label="Band of green lawn grass"/>
    <path d="M330 30 C 345 30, 340 6, 362 6 L 615 6 L 615 30 Z" fill="#58585b"/>
  </svg>
  <div class="website">www.meadowtrim.com</div>
</section>

<section class="card card-back" aria-label="Business card back">
  <div class="wordmark"><span>meadowtrim</span><span class="wordmark-dot"></span></div>
  <p class="services">
    Lawn Mowing <span class="services-dot"></span>Garden Maintenance<br>
    Clean ups &amp; Some Property Maintenance.
  </p>
</section>

</body>
</html>
```